Business Card Design

I am a Accounting/Bookkeeping company.  As a sideline, I am also a Notary so I would like that somewhere, either in front or perhaps the backside for the notary business.
I found a standard card I really like but didn't like the "little man" standing on the scale.
I love the colors so I am wondering if you would be able to duplicate this without the man and perhaps money or something appropriate on this side of scale
I also need help on the font.  I tend to like feminine styles but am told they are too hard to read.

Target Market(s)
Small businesses, Individuals
Industry/Entity Type
Business
Contact Information for Business Card
The Tidy Ledgerwright
Keeping every column in quiet order
Marisol (Pebbleton) Varnaccio
Accounting Associate
Certified FiscalTrail CountExpert
Notary Public
Serving Marlowe Valley                            415-362-9184
marisol.varnaccio@plumpost.example

Requirements
Must have
- I would like a glossy card

```html
<!DOCTYPE html>
<html lang="en">
<head>
<meta charset="utf-8">
<title>The Tidy Ledgerwright – Business Card</title>
<link rel="stylesheet" href="https://fonts.googleapis.com/css2?family=Cinzel:wght@400;600&display=swap">
<style>
  :root {
    --backdrop: #ecebe6;
    --card-olive: #b3a733;
    --card-olive-deep: #a89c2c;
    --card-ink: #ffffff;
    --emblem-tone: #c9bf62;
  }
  html, body {
    margin: 0;
    width: 1200px;
    height: 892px;
    overflow: hidden;
    background: var(--backdrop);
  }
  .canvas {
    position: relative;
    width: 1200px;
    height: 892px;
    display: flex;
    align-items: center;
    justify-content: center;
  }
  .business-card {
    position: relative;
    width: 1000px;
    height: 572px;
    background: linear-gradient(135deg, var(--card-olive) 0%, var(--card-olive) 60%, var(--card-olive-deep) 100%);
    color: var(--card-ink);
    font-family: "Cinzel", serif;
    box-shadow: 0 10px 30px rgba(0,0,0,0.18);
    overflow: hidden;
  }
  .brand-name {
    position: absolute;
    left: 150px;
    top: 40px;
    margin: 0;
    font-size: 58px;
    font-weight: 600;
    letter-spacing: 1px;
    line-height: 1;
    white-space: nowrap;
  }
  .tagline {
    position: absolute;
    left: 270px;
    top: 104px;
    margin: 0;
    font-size: 24px;
    letter-spacing: 1px;
    white-space: nowrap;
  }
  .holder-name {
    position: absolute;
    left: 120px;
    top: 160px;
    margin: 0;
    font-size: 28px;
    font-weight: 400;
    white-space: nowrap;
  }
  .credentials {
    position: absolute;
    left: 92px;
    top: 218px;
    margin: 0;
    padding: 0;
    list-style: none;
    font-size: 22px;
    line-height: 1.15;
  }
  .service-area {
    position: absolute;
    left: 40px;
    top: 360px;
    margin: 0;
    font-size: 24px;
    white-space: nowrap;
  }
  .contact {
    position: absolute;
    right: 36px;
    bottom: 48px;
    text-align: right;
    font-size: 18px;
    line-height: 1.5;
  }
  .contact p { margin: 0; }
  .scale-emblem {
    position: absolute;
    right: 60px;
    top: 230px;
    width: 240px;
    height: 180px;
  }
</style>
</head>
<body>
<main class="canvas">
  <article class="business-card">
    <h1 class="brand-name">The Tidy Ledgerwright</h1>
    <p class="tagline">Keeping every column in quiet order</p>
    <h2 class="holder-name">Marisol (Pebbleton) Varnaccio</h2>
    <ul class="credentials">
      <li>Accounting Associate</li>
      <li>Certified FiscalTrail CountExpert</li>
      <li>Notary Public</li>
    </ul>
    <p class="service-area">Serving Marlowe Valley</p>
    <svg class="scale-emblem" role="img" aria-label="Balance scale illustration" viewBox="0 0 240 180">
      <rect width="240" height="180" rx="10" fill="var(--emblem-tone)"/>
    </svg>
    <div class="contact">
      <p class="phone">T:415 362 9184</p>
      <p class="email">marisol.varnaccio@plumpost.example</p>
    </div>
  </article>
</main>
</body>
</html>
```